Harlow Learning Advancement Trust Council (HLATC) Fall Appeal Mailing

HLATC is a nonprofit educational fund that raises money annually from the parent community to provide enrichment programming in the Brindle Public Schools (in Massachusetts). Our intention is to revamp our fall appeal mailing to a more interesting/reader friendly format. In the past, we have simply mailed an appeal letter on our letterhead explaining what we do to all families in the school system. Our thought is to redesign our mailing by folding an 8 and 1/2 by 11 sheet of paper in half, creating a folding card that opens from the bottom which will fit into a 6x9 envelope. Rather than simply including text, we want to try to convey our message using more graphics and colors. We have the start of a design that I am sending you that will give you an idea of the information that we want to convey, our logo and also contains more information about what we do. It is only a working draft, and although our Board does like the concept, we are open to other ideas as well. Our school colors are maroon and white, and our logo is the outline of a maroon triangle with HLATC underneath. The colors of the mailing should incorporate the maroon, although other colors should definitely be included. We want it visually appealing without too much verbiage. Our tagline is - 100% of Parents Supporting 100% of Brindle School Children.

Target Market(s)

Our target audience is parents of school aged children. HLATC funds provide programming for all grades - pre-K through 12.

Industry/Entity Type

School

Requirements
Must have
• Eye catching with a message that is clear... Send in your donation today! or something along those lines. We will enclose a donation card and return envelope, so there is no need to include any donation instructions. For parents who are new to the district or want to read more, text, like what appears on the back page of the uploaded file should be included. Colors should incorporate the maroon color from our logo, but can include any other colors as well.

```html
<!DOCTYPE html>
<html lang="en">
<head>
<meta charset="utf-8">
<title>HLATC Fall Appeal – Did You Know</title>
<link rel="stylesheet" href="https://fonts.googleapis.com/css2?family=Source+Sans+3:ital,wght@0,700;0,800;1,700&display=swap">
<style>
  :root {
    --maroon: #8c1b35;
    --ink: #8c1b35;
    --rule: #555555;
    --paper: #ffffff;
    --outline: #5a5a5a;
  }
  * { margin: 0; padding: 0; box-sizing: border-box; }
  html, body { width: 930px; height: 1200px; overflow: hidden; background: var(--paper); }
  .card {
    position: relative;
    width: 930px;
    height: 1200px;
    font-family: "Source Sans 3", "Myriad Pro", Arial, sans-serif;
  }
  .art { position: absolute; inset: 0; }
  .headline {
    font-family: "Source Sans 3", Arial, sans-serif;
    font-weight: 800;
    font-size: 78px;
    fill: var(--maroon);
  }
  .appeal {
    position: absolute;
    left: 470px; top: 544px;
    width: 440px;
    text-align: center;
    color: var(--maroon);
    font-weight: 800;
    font-size: 28px;
    line-height: 34px;
  }
  .fold-line {
    position: absolute;
    left: 0; right: 0;
    top: 595px;
    border-top: 3px dashed var(--rule);
  }
  .info-panel {
    position: absolute;
    left: 64px; top: 658px;
    width: 800px; height: 484px;
    border: 10px solid var(--maroon);
    border-radius: 4px;
  }
  .info-text {
    position: absolute;
    left: 86px; top: 686px;
    color: var(--ink);
    font-style: italic;
    font-weight: 700;
    font-size: 19px;
    line-height: 25px;
    white-space: nowrap;
  }
  .info-text h2 {
    font-size: 19px;
    font-weight: 700;
    text-transform: uppercase;
  }
  .info-text ul { list-style: none; }
  .info-text li { position: relative; padding-left: 34px; }
  .info-text li::before {
    content: "·";
    position: absolute; left: 0;
    font-style: normal;
  }
  .info-text .types { margin-top: 40px; }
  .tagline {
    position: absolute;
    left: 262px; top: 1104px;
    color: var(--maroon);
    font-style: italic;
    font-weight: 700;
    font-size: 14px;
    white-space: nowrap;
  }
  .brand-name {
    position: absolute;
    left: 742px; top: 1090px;
    color: var(--maroon);
    font-weight: 700;
    font-size: 22px;
    letter-spacing: 1px;
  }
</style>
</head>
<body>
<main class="card">
  <svg class="art" width="930" height="1200" viewBox="0 0 930 1200" aria-hidden="true">
    <defs>
      <radialGradient id="g-red"><stop offset="0" stop-color="#ffb3c4"/><stop offset="1" stop-color="#f2666a"/></radialGradient>
      <radialGradient id="g-orange"><stop offset="0" stop-color="#ffe6c4"/><stop offset="1" stop-color="#fcbd6c"/></radialGradient>
      <radialGradient id="g-green"><stop offset="0" stop-color="#e4ffd8"/><stop offset="1" stop-color="#a6f36a"/></radialGradient>
      <radialGradient id="g-purple"><stop offset="0" stop-color="#fbe6ff"/><stop offset="1" stop-color="#d88cf3"/></radialGradient>
      <radialGradient id="g-brown"><stop offset="0" stop-color="#ffb5a0"/><stop offset="1" stop-color="#c77a5c"/></radialGradient>
      <radialGradient id="g-aqua"><stop offset="0" stop-color="#f2fffc"/><stop offset="1" stop-color="#b2f5e6"/></radialGradient>
    </defs>
    <g stroke="var(--outline)" stroke-width="1.5">
      <circle cx="135" cy="128" r="101" fill="url(#g-red)"/>
      <circle cx="765" cy="166" r="133" fill="url(#g-orange)"/>
      <circle cx="476" cy="312" r="135" fill="url(#g-green)"/>
      <circle cx="174" cy="410" r="107" fill="url(#g-purple)"/>
      <circle cx="359" cy="475" r="86" fill="url(#g-brown)"/>
      <circle cx="798" cy="433" r="99" fill="url(#g-aqua)"/>
    </g>
    <text class="headline" x="297" y="225" text-anchor="middle" dominant-baseline="central" transform="rotate(180 297 225)">Know...</text>
    <text class="headline" x="531" y="333" text-anchor="middle" dominant-baseline="central" transform="rotate(180 531 333)">You</text>
    <text class="headline" x="694" y="438" text-anchor="middle" dominant-baseline="central" transform="rotate(180 694 438)">Did</text>
  </svg>

  <p class="appeal">Send in your donation today!</p>

  <div class="fold-line"></div>

  <div class="info-panel"></div>

  <svg class="art" width="930" height="1200" viewBox="0 0 930 1200" aria-hidden="true">
    <g stroke="var(--outline)" stroke-width="1.5">
      <circle cx="800" cy="826" r="48" fill="url(#g-aqua)"/>
      <circle cx="190" cy="1056" r="62" fill="url(#g-red)"/>
      <circle cx="588" cy="1045" r="50" fill="url(#g-green)"/>
    </g>
  </svg>

  <section class="info-text">
    <h2>Mission of the Harlow Learning Advancement Trust Council</h2>
    <ul>
      <li>To award enrichment grants submitted by administrators, teachers, students and<br>parents, subject to School Committee approval</li>
      <li>To solicit tax-deductible donations on an annual basis for school enrichment<br>programs in grades K-12</li>
    </ul>
    <div class="types">
      <h2>Types of Grants</h2>
      <ul>
        <li>Mini-grants for equipment and supplies for classroom projects, guest artists or<br>speakers, and educational field trips</li>
        <li>Project grants for larger expenditures that advance system-wide goals</li>
        <li>Teacher development grants through the Professional Development Academy</li>
        <li>Collaborative programs with PTO Creative Arts and Science Councils</li>
      </ul>
    </div>
  </section>

  <p class="tagline">100% of Parents Supporting 100% of Brindle School Children</p>
  <div class="brand-name">HLATC</div>
</main>
</body>
</html>
```